Business Broker Website

Hi.
I need a new design done for a business broker website. An example of the style of website I like is https://marlowpartners.example/
The menu needs to be :
* Home
* Businesses for Sale
* What we do
* Our people
* Industries
* Blog
* Confidentiality
* Contact
The home page needs to include a section saying 'businesses sold' with each having a photo, heading and short description. It also needs to have a place to show a video which I have attached so you can take a screenshot to put it on the page.
The content on the home page needs to be as follows:
Venture Transfer Partners are a boutique brokerage business, specializing in the sales and marketing of SME businesses throughout Queensland and, the Northern Territory
who we are
Welcome to Venture Transfer Partners. Our specialization is in the marketing and acquisition of closely held businesses throughout Queensland and the Northern Territory. We concentrate in SME businesses in the turnovers of approximately $1,000,000 to $10,000,000 +.
The combined business experience and industry knowledge of our principal is unparalleled and fully committed to a “customer first always” approach to doing business.
Our seller’s benefit from a multi-faceted strategic marketing plan, custom prepared for each seller, no two marketing campaigns are the same. This assures maximum exposure to well-qualified Buyers, while strictly maintaining confidentiality.
We have the comprehensive knowledge and resources to help our Buyers identify their perfect business acquisition– perhaps even if that business is not currently listed for sale!
"the whole secret of a successful life is to find out what is one's destiny to do, and then do it." walter pimm
Target Market(s)
people looking to buy or sell businesses
Number of Pages Required
1 page
Look and feel

```html
<!DOCTYPE html>
<html lang="en">
<head>
<meta charset="utf-8">
<title>Venture Transfer Partners</title>
<link href="https://fonts.googleapis.com/css2?family=Poppins:ital,wght@0,300;0,400;0,500;0,600;0,700;1,400&display=swap" rel="stylesheet">
<style>
:root{
  --purple:#5b3e8f;
  --purple-deep:#4a2f7a;
  --ink:#2b2b2b;
  --charcoal:#3a3a3a;
  --grey:#6f6f6f;
  --line:#9a9a9a;
  --white:#ffffff;
  --footer-bar:#1b1b1b;
}
*{box-sizing:border-box;margin:0;padding:0}
html,body{width:1200px;height:3909px;overflow:hidden}
body{font-family:'Poppins',sans-serif;color:var(--ink);background:var(--white);position:relative}
.abs{position:absolute}
a{color:inherit;text-decoration:none}

/* header */
.topbar{position:absolute;left:0;top:0;width:1200px;height:82px}
.brand{position:absolute;left:111px;top:18px;display:flex;align-items:center;gap:12px}
.brand-dot{width:44px;height:44px;border-radius:50%;background:var(--purple)}
.brand-name{font-size:24px;font-weight:600;color:var(--purple);line-height:1}
.contact-item{position:absolute;top:16px;display:flex;align-items:center;gap:16px}
.contact-icon{width:50px;height:50px;border-radius:50%;background:var(--charcoal);display:flex;align-items:center;justify-content:center}
.contact-label{font-size:13px;color:var(--purple);line-height:20px}
.contact-value{font-size:17px;color:var(--ink);line-height:22px}

.nav{position:absolute;left:0;top:82px;width:1200px;height:52px;background:var(--purple)}
.nav ul{list-style:none;display:flex;position:absolute;left:111px;top:0;height:52px}
.nav li{font-size:16px;color:var(--white);height:52px;line-height:52px;padding:0 20px}
.nav li.active{background:var(--charcoal)}

/* hero */
.hero{position:absolute;left:0;top:134px;width:1200px;height:564px;
  background:linear-gradient(90deg,#f1f1f2 0%,#ececee 38%,#d9dadd 55%,#b9b6b3 72%,#8d8680 100%)}
.hero-title{position:absolute;left:110px;top:168px;font-size:34px;font-weight:600;color:var(--purple)}
.hero-text{position:absolute;left:110px;top:220px;width:500px;font-size:13.5px;line-height:32px;color:#4a4a4a}
.btn{position:absolute;display:flex;align-items:center;justify-content:center;gap:12px;height:56px;border-radius:4px;font-size:16px;font-weight:600;color:var(--white);text-transform:uppercase}
.btn-purple{background:var(--purple)}
.btn-dark{background:var(--charcoal)}
.btn-mark{width:30px;height:30px;border-radius:50%;background:rgba(255,255,255,.9)}

/* who */
.who-wash{position:absolute;left:0;top:698px;width:365px;height:354px;background:#f3f3f5}
.frame{position:absolute;border:1.5px solid var(--purple)}
.video{position:absolute;display:flex;align-items:center;justify-content:center}
.play{width:84px;height:84px;border-radius:50%;background:rgba(255,255,255,.92);display:flex;align-items:center;justify-content:center}
.section-title{font-size:43px;font-weight:600;line-height:1.1}
.who-title{position:absolute;left:625px;top:826px;color:var(--purple)}
.rule{position:absolute;height:4px}
.who-list{position:absolute;left:622px;top:918px;width:520px;list-style:none}
.who-list li{position:relative;padding-left:19px;font-size:12.5px;line-height:22px;color:#555;margin-bottom:12px}
.who-list li svg{position:absolute;left:0;top:5px}

/* sold */
.sold{position:absolute;left:0;top:1388px;width:1200px;height:700px;background:var(--purple)}
.sold-title{position:absolute;left:0;width:1200px;top:54px;text-align:center;color:var(--white)}
.card{position:absolute;top:161px;width:314px}
.card-img{width:314px;height:262px;border-radius:14px}
.card h3{margin-top:18px;font-size:16px;font-weight:600;color:var(--white)}
.card p{margin-top:6px;font-size:12.5px;line-height:26px;color:#eee9f5}
.arrow{position:absolute;top:290px}

/* what we do */
.what-title{position:absolute;left:0;width:1200px;top:2162px;text-align:center;color:var(--purple)}
.service{position:absolute;top:2275px;width:332px;height:326px;text-align:center}
.service.featured{border:2px solid var(--purple);border-radius:10px;background:var(--white)}
.service-icon{margin:34px auto 0;width:115px;height:102px;border-radius:6px;background:var(--white);box-shadow:0 2px 10px rgba(0,0,0,.12);display:flex;align-items:center;justify-content:center}
.service.featured .service-icon{box-shadow:none}
.service h3{margin-top:24px;font-size:15px;font-weight:600;color:var(--ink)}
.service p{margin:8px auto 0;width:306px;font-size:12.5px;line-height:25px;color:var(--grey)}
.service .more{display:inline-block;margin-top:18px;font-size:14px;font-weight:500;color:var(--purple);text-decoration:underline}

/* quote */
.quote-band{position:absolute;left:0;top:2708px;width:1200px;height:204px;background:#454545}
.quote-photo{position:absolute;left:660px;top:2685px;width:540px;height:227px;
  background:linear-gradient(110deg,#5b5e66 0%,#8b8f99 40%,#c5c3c2 65%,#3b3c40 100%);
  clip-path:polygon(12% 0,100% 0,100% 100%,0 100%)}
.quote-text{position:absolute;left:108px;top:2750px;width:620px;font-size:20px;font-style:italic;line-height:34px;color:var(--white)}
.quote-name{position:absolute;left:108px;top:2826px;font-size:28px;color:var(--white)}

/* contact */
.contact-title{position:absolute;left:0;width:1200px;top:2970px;text-align:center;color:var(--ink)}
.contact-intro{position:absolute;left:270px;width:660px;top:3057px;text-align:center;font-size:13.5px;line-height:26px;color:var(--grey)}
.field{position:absolute;border-bottom:2px solid var(--line);font-size:15px;color:#6a6a6a;padding-bottom:10px}

/* footer */
.footer{position:absolute;left:0;top:3560px;width:1200px;height:290px;background:linear-gradient(180deg,#2c2c2c,#222)}
.footer-brand{position:absolute;left:115px;top:50px;display:flex;align-items:center;gap:12px}
.footer-brand .brand-dot{background:var(--white);width:40px;height:40px}
.footer-brand .brand-name{color:var(--white);font-size:22px}
.footer-about{position:absolute;left:110px;top:122px;width:370px;font-size:12px;line-height:26px;color:var(--white)}
.footer-head{position:absolute;top:68px;font-size:17px;font-weight:600;color:var(--white)}
.links{position:absolute;top:114px;list-style:none}
.links li{font-size:13.5px;line-height:29.5px;color:var(--white);display:flex;align-items:center;gap:9px}
.footer-phone{position:absolute;left:898px;top:108px;display:flex;align-items:center;gap:8px;font-size:15px;font-weight:600;color:var(--white)}
.phone-ring{width:32px;height:32px;border-radius:50%;border:1.5px solid var(--white);display:flex;align-items:center;justify-content:center}
.socials{position:absolute;left:906px;top:173px;display:flex;gap:15px}
.socials span{width:32px;height:32px;background:var(--purple);display:block}
.footer-bar{position:absolute;left:0;top:3850px;width:1200px;height:59px;background:var(--footer-bar);text-align:center;line-height:59px;font-size:14px;font-weight:600;color:var(--white)}
</style>
</head>
<body>

<header class="topbar">
  <div class="brand"><span class="brand-dot"></span><span class="brand-name">Venture Transfer Partners</span></div>
  <div class="contact-item" style="left:519px">
    <div class="contact-icon"><svg width="20" height="20" viewBox="0 0 24 24"><path fill="#fff" d="M6.6 10.8a15 15 0 0 0 6.6 6.6l2.2-2.2a1 1 0 0 1 1-.25 11.4 11.4 0 0 0 3.6.57 1 1 0 0 1 1 1V20a1 1 0 0 1-1 1A17 17 0 0 1 3 4a1 1 0 0 1 1-1h3.5a1 1 0 0 1 1 1c0 1.25.2 2.45.57 3.57a1 1 0 0 1-.25 1z"/></svg></div>
    <div><div class="contact-label">Call Now</div><div class="contact-value">+1 (555) 014 2290</div></div>
  </div>
  <div class="contact-item" style="left:766px">
    <div class="contact-icon"><svg width="20" height="16" viewBox="0 0 20 16"><rect x="0" y="0" width="20" height="16" rx="2" fill="#fff"/><path d="M1 2l9 7 9-7" stroke="#3a3a3a" stroke-width="2" fill="none"/></svg></div>
    <div><div class="contact-label">Email Now</div><div class="contact-value">hello@venturetransfer.example</div></div>
  </div>
</header>

<nav class="nav">
  <ul>
    <li class="active">Home</li><li>Businesses for Sale</li><li>What we do</li><li>Our people</li><li>Industries</li><li>Blog</li><li>Confidentiality</li><li>Contact</li>
  </ul>
</nav>

<section class="hero" role="img" aria-label="Photo of two smiling colleagues working at laptops in a bright office">
  <h1 class="hero-title">Venture Transfer Partners.</h1>
  <p class="hero-text">Venture Transfer Partners are a boutique brokerage business, specializing in the sales and marketing of SME businesses throughout Queensland and, the Northern Territory</p>
  <a class="btn btn-purple" style="left:111px;top:334px;width:225px"><span class="btn-mark"></span>Get Started</a>
  <svg class="abs" style="left:587px;top:518px" width="26" height="16" viewBox="0 0 26 16"><path d="M2 2l11 11L24 2" stroke="#2b2b2b" stroke-width="3" fill="none"/></svg>
</section>

<section class="who">
  <div class="who-wash"></div>
  <div class="frame" style="left:212px;top:794px;width:370px;height:370px"></div>
  <div class="video" role="img" aria-label="Video screenshot: colleagues in discussion around a meeting table" style="left:112px;top:828px;width:446px;height:435px;background:linear-gradient(135deg,#3c4656 0%,#2a3140 45%,#1a1f28 100%)">
    <span class="play"><svg width="30" height="34" viewBox="0 0 30 34"><path d="M4 2l24 15L4 32z" fill="#5b3e8f"/></svg></span>
  </div>
  <div class="frame" style="left:70px;top:1095px;width:211px;height:211px"></div>
  <h2 class="section-title who-title">Who We Are</h2>
  <div class="rule" style="left:628px;top:889px;width:104px;background:var(--purple)"></div>
  <ul class="who-list">
    <li><svg width="12" height="12" viewBox="0 0 12 12"><circle cx="6" cy="6" r="6" fill="#5b3e8f"/><path d="M3 6.2l2 2 4-4" stroke="#fff" stroke-width="1.6" fill="none"/></svg>Welcome to Venture Transfer Partners. Our specialization is in the marketing and acquisition of closely held businesses throughout Queensland and the Northern Territory. We concentrate in SME businesses in the turnovers of approximately $1,000,000 to $10,000,000 +.</li>
    <li><svg width="12" height="12" viewBox="0 0 12 12"><circle cx="6" cy="6" r="6" fill="#5b3e8f"/><path d="M3 6.2l2 2 4-4" stroke="#fff" stroke-width="1.6" fill="none"/></svg>The combined business experience and industry knowledge of our principal is unparalleled and fully committed to a “customer first always” approach to doing business.</li>
    <li><svg width="12" height="12" viewBox="0 0 12 12"><circle cx="6" cy="6" r="6" fill="#5b3e8f"/><path d="M3 6.2l2 2 4-4" stroke="#fff" stroke-width="1.6" fill="none"/></svg>Our seller’s benefit from a multi-faceted strategic marketing plan, custom prepared for each seller, no two marketing campaigns are the same. This assures maximum exposure to well-qualified Buyers, while strictly maintaining confidentiality.</li>
    <li><svg width="12" height="12" viewBox="0 0 12 12"><circle cx="6" cy="6" r="6" fill="#5b3e8f"/><path d="M3 6.2l2 2 4-4" stroke="#fff" stroke-width="1.6" fill="none"/></svg>We have the comprehensive knowledge and resources to help our Buyers identify their perfect business acquisition – perhaps even if that business is not currently listed for sale!</li>
  </ul>
  <a class="btn btn-purple" style="left:628px;top:1292px;width:225px"><span class="btn-mark"></span>Read More</a>
</section>

<section class="sold">
  <h2 class="section-title sold-title">Businesses Sold</h2>
  <div class="rule" style="left:547px;top:119px;width:106px;background:var(--white)"></div>
  <svg class="arrow" style="left:74px" width="18" height="30" viewBox="0 0 18 30"><path d="M15 2L3 15l12 13" stroke="#fff" stroke-width="3" fill="none"/></svg>
  <svg class="arrow" style="left:1100px" width="18" height="30" viewBox="0 0 18 30"><path d="M3 2l12 13L3 28" stroke="#fff" stroke-width="3" fill="none"/></svg>
  <article class="card" style="left:111px">
    <div class="card-img" role="img" aria-label="Photo of a team gathered around a laptop in an office" style="background:linear-gradient(135deg,#d7d8da,#9a9186 60%,#5a5450)"></div>
    <h3>Lorem ipsum dolor sit amet</h3>
    <p>Sed do eiusmod tempor incididunt ut labore et dolore magna aliqua. Ut enim ad minim veniam, quis nostrud exercitation</p>
  </article>
  <article class="card" style="left:442px">
    <div class="card-img" role="img" aria-label="Photo of a group working at a table under a hanging light bulb" style="background:linear-gradient(135deg,#4b4a3c,#7a6a4e 50%,#3c4a35)"></div>
    <h3>Lorem ipsum dolor sit amet</h3>
    <p>Sed do eiusmod tempor incididunt ut labore et dolore magna aliqua. Ut enim ad minim veniam, quis nostrud exercitation</p>
  </article>
  <article class="card" style="left:772px">
    <div class="card-img" role="img" aria-label="Photo of two colleagues reviewing a notebook together" style="background:linear-gradient(135deg,#e6e8ea,#a9b0b8 55%,#6d7580)"></div>
    <h3>Lorem ipsum dolor sit amet</h3>
    <p>Sed do eiusmod tempor incididunt ut labore et dolore magna aliqua. Ut enim ad minim veniam, quis nostrud exercitation</p>
  </article>
  <a class="btn btn-dark" style="left:492px;top:584px;width:216px"><span class="btn-mark"></span>View More</a>
</section>

<section class="what">
  <h2 class="section-title what-title">What We Do</h2>
  <div class="rule" style="left:545px;top:2230px;width:110px;background:var(--charcoal)"></div>
  <div class="service" style="left:99px">
    <div class="service-icon"><svg width="70" height="70" viewBox="0 0 70 70" fill="none" stroke="#5b3e8f" stroke-width="2"><rect x="8" y="10" width="34" height="44" rx="2"/><path d="M14 20h20M14 28h14M14 36h10"/><rect x="26" y="34" width="36" height="24" rx="2"/><path d="M38 34v-5h12v5M26 44h36"/><rect x="40" y="41" width="8" height="6"/></svg></div>
    <h3>Lorem ipsum dolor sit</h3>
    <p>Sed do eiusmod tempor incididunt ut labore et dolore magna aliqua. Ut enim veniam, quis nostrud exercitation ullamco</p>
  </div>
  <div class="service featured" style="left:435px">
    <div class="service-icon"><svg width="80" height="50" viewBox="0 0 80 50" fill="none" stroke="#5b3e8f" stroke-width="2"><path d="M2 10l12-4 10 6 10-4h8l16 4 10-2 10 4-2 20-10 2-14 12a4 4 0 0 1-6-1l-4 2a4 4 0 0 1-6-2l-4 2a4 4 0 0 1-6-3l-4 1a4 4 0 0 1-4-5L6 30z"/><path d="M34 8l-10 12a4 4 0 0 0 6 4l10-8 16 14"/></svg></div>
    <h3>Lorem ipsum dolor sit</h3>
    <p>Sed do eiusmod tempor incididunt ut labore et dolore magna aliqua. Ut enim veniam, quis nostrud exercitation ullamco</p>
    <a class="more">Read More</a>
  </div>
  <div class="service" style="left:769px">
    <div class="service-icon"><svg width="70" height="70" viewBox="0 0 70 70" fill="none" stroke="#5b3e8f" stroke-width="2"><rect x="8" y="8" width="14" height="14"/><path d="M11 15l3 3 5-6"/><rect x="48" y="28" width="14" height="14"/><path d="M51 35l3 3 5-6"/><rect x="8" y="48" width="14" height="14"/><path d="M11 55l3 3 5-6"/><circle cx="35" cy="35" r="9"/><circle cx="35" cy="35" r="4"/><path d="M30 12a24 24 0 0 1 20 8M26 60a24 24 0 0 0 20-4M12 30v10"/></svg></div>
    <h3>Lorem ipsum dolor sit</h3>
    <p>Sed do eiusmod tempor incididunt ut labore et dolore magna aliqua. Ut enim veniam, quis nostrud exercitation ullamco</p>
  </div>
</section>

<section class="quote">
  <div class="quote-band"></div>
  <div class="quote-photo" role="img" aria-label="Photo of two business people shaking hands"></div>
  <p class="quote-text">The whole secret of a successful life is to find out what is one’s destiny to do, and then do it.</p>
  <p class="quote-name">Walter Pimm</p>
</section>

<section class="contact">
  <h2 class="section-title contact-title">Contact Us</h2>
  <div class="rule" style="left:545px;top:3040px;width:110px;background:var(--charcoal)"></div>
  <p class="contact-intro">Lorem ipsum dolor sit amet, consectetur adipiscing elit, sed do eiusmod tempor incididunt ut labore et dolore magna aliqua. Ut enim ad</p>
  <div class="field" style="left:228px;top:3143px;width:350px">First Name</div>
  <div class="field" style="left:623px;top:3143px;width:350px">Last Name</div>
  <div class="field" style="left:228px;top:3213px;width:350px">Email Address</div>
  <div class="field" style="left:623px;top:3213px;width:350px">Phone Number</div>
  <div class="field" style="left:228px;top:3283px;width:740px;height:102px">Message</div>
  <a class="btn btn-purple" style="left:487px;top:3440px;width:226px;font-size:15px">Submit</a>
</section>

<footer class="footer">
  <div class="footer-brand"><span class="brand-dot"></span><span class="brand-name">Venture Transfer Partners</span></div>
  <p class="footer-about">Welcome to Venture Transfer Partners. Our specialization is in the marketing acquisition of closely held businesses throughout Queensland and the Northern Territory. We concentrate in SME businesses in the turnovers of approximately $1,000,000 to $10,000,000 +.</p>
  <h4 class="footer-head" style="left:537px">Quick Links</h4>
  <ul class="links" style="left:537px">
    <li><svg width="9" height="9" viewBox="0 0 9 9"><path d="M1 1l3 3.5L1 8M5 1l3 3.5L5 8" stroke="#fff" fill="none"/></svg>Home</li>
    <li><svg width="9" height="9" viewBox="0 0 9 9"><path d="M1 1l3 3.5L1 8M5 1l3 3.5L5 8" stroke="#fff" fill="none"/></svg>Businesses for Sale</li>
    <li><svg width="9" height="9" viewBox="0 0 9 9"><path d="M1 1l3 3.5L1 8M5 1l3 3.5L5 8" stroke="#fff" fill="none"/></svg>What we do</li>
    <li><svg width="9" height="9" viewBox="0 0 9 9"><path d="M1 1l3 3.5L1 8M5 1l3 3.5L5 8" stroke="#fff" fill="none"/></svg>Our people</li>
    <li><svg width="9" height="9" viewBox="0 0 9 9"><path d="M1 1l3 3.5L1 8M5 1l3 3.5L5 8" stroke="#fff" fill="none"/></svg>Industries</li>
  </ul>
  <ul class="links" style="left:722px">
    <li><svg width="9" height="9" viewBox="0 0 9 9"><path d="M1 1l3 3.5L1 8M5 1l3 3.5L5 8" stroke="#fff" fill="none"/></svg>Blog</li>
    <li><svg width="9" height="9" viewBox="0 0 9 9"><path d="M1 1l3 3.5L1 8M5 1l3 3.5L5 8" stroke="#fff" fill="none"/></svg>Confidentiality</li>
    <li><svg width="9" height="9" viewBox="0 0 9 9"><path d="M1 1l3 3.5L1 8M5 1l3 3.5L5 8" stroke="#fff" fill="none"/></svg>Contact</li>
  </ul>
  <h4 class="footer-head" style="left:895px">Contact Us</h4>
  <div class="footer-phone"><span class="phone-ring"><svg width="14" height="14" viewBox="0 0 24 24"><path fill="#fff" d="M6.6 10.8a15 15 0 0 0 6.6 6.6l2.2-2.2a1 1 0 0 1 1-.25 11.4 11.4 0 0 0 3.6.57 1 1 0 0 1 1 1V20a1 1 0 0 1-1 1A17 17 0 0 1 3 4a1 1 0 0 1 1-1h3.5a1 1 0 0 1 1 1c0 1.25.2 2.45.57 3.57a1 1 0 0 1-.25 1z"/></svg></span>+1 555 014 2290</div>
  <div class="socials" aria-label="Social links"><span></span><span></span><span></span><span></span></div>
</footer>
<div class="footer-bar">Venture Transfer Partners © 2022 All Rights Reserved</div>

</body>
</html>
```